Marlow Realty Real Estate Brokerage Recruiting Flyer

We are a real estate brokerage looking to hire more real estate agents. We need to list everything we have to offer as a company so real estate agents will join our company. this is our company website: www.Marlowrealty.example .

100% COMMISSION NO MONTHLY FEE
$450 Flat Transaction FEE

What We Offer:
24/7 Office Access
Free E & O Insurance for 1st Year
Free Online CE and PLE
Free 1,000 Business Cards
Free Professional Social Media Marketing
Free Printing, Scanning, and Copies
Free Buyer and Seller Presentation Packages
Free Filquay Cloud Based Document Management Access
Access to our Internal Brokerage Forum
Company Profit Sharing!
Private Offices Available to Rent

*Lead Generation Software with over 3,000 Leads
*10 Leads to Start
* Free Personal CRM and Website
*Restrictions and Rules apply

Company Address:
4817 Amberfield Road
Suite 512
Fairfax, VA 22194
Phone: 703-555-0147
email: info@marlowrealty.example

Target Market(s)

Real Estate Agents

Industry/Entity Type

Real Estate

Colors
0555a3
ffffff

Requirements
Must have
• 100% COMMISSION NO MONTHLY FEE
$450 Flat Transaction FEE

What We Offer:
24/7 Office Access
Free Online CE and PLE
Free 1,000 Business Cards
Company Profit Sharing!

*10 Leads to Start

Company Address:
4817 Amberfield Road
Suite 512
Fairfax, VA 22194
Phone: 703-555-0147

```html
<!DOCTYPE html>
<html lang="en">
<head>
<meta charset="utf-8">
<title>Marlow Realty – Agent Recruiting Flyer</title>
<link href="https://fonts.googleapis.com/css2?family=Bebas+Neue&family=Roboto:wght@400;500;700&display=swap" rel="stylesheet">
<style>
  :root{
    --navy:#1b2e6e;
    --brand-blue:#0555a3;
    --sky-blue:#1e8fd8;
    --pale-sky:#d6eef5;
    --leaf:#6cbf3a;
    --leaf-dark:#4fa12a;
    --sun-yellow:#f3e81a;
    --ink-grey:#4d4d4d;
    --panel-grey:#e4e4e4;
    --rule-grey:#9a9a9a;
    --skyline:#ececef;
    --white:#ffffff;
    --stage:#e8e8e8;
    --footer-ink:#222222;
  }
  *{box-sizing:border-box;margin:0;padding:0}
  html,body{width:1200px;height:880px;overflow:hidden}
  body{background:var(--stage);font-family:"Roboto",Arial,sans-serif;position:relative}

  .flyer{position:absolute;left:300px;top:20px;width:600px;height:840px;background:var(--white);overflow:hidden}

  .hero{position:absolute;left:0;top:0;width:600px;height:340px;
    background:linear-gradient(180deg,var(--pale-sky) 0%,#e6f4f8 70%,var(--white) 100%)}
  .brand{position:absolute;left:28px;top:44px;display:flex;align-items:center;gap:10px}
  .brand-mark{width:22px;height:22px;background:var(--navy)}
  .brand-name{font-weight:500;font-size:30px;color:var(--navy);letter-spacing:1px}

  .hero-art{position:absolute;left:0;top:118px;width:330px;height:215px;border-radius:0 40px 0 0;
    background:linear-gradient(160deg,#bfe0ea 0%,#9fc9a6 55%,#7cc24a 100%)}

  .commission{position:absolute;left:370px;top:108px}
  .commission .pct{font-family:"Bebas Neue",Impact,sans-serif;font-size:66px;line-height:60px;color:var(--sky-blue)}
  .commission .line{font-weight:700;font-size:24px;line-height:28px;color:var(--navy)}

  .fee-band{position:absolute;left:300px;top:240px;width:300px;height:62px;background:var(--leaf);border-radius:30px 0 0 30px}
  .fee-band .amount{position:absolute;left:70px;top:6px;font-family:"Bebas Neue",Impact,sans-serif;font-size:48px;line-height:52px;color:var(--white)}
  .fee-band .label{position:absolute;left:153px;top:5px;font-weight:500;font-size:18px;line-height:18px;color:var(--sun-yellow)}

  .offer-heading{position:absolute;left:30px;top:350px;width:545px;display:flex;align-items:center;gap:10px}
  .offer-heading h2{font-size:21px;font-weight:700;color:var(--navy);white-space:nowrap}
  .offer-heading .rule{flex:1;height:2px;background:var(--navy)}

  .offer-list{position:absolute;left:18px;top:380px;width:300px;height:345px;background:linear-gradient(90deg,var(--panel-grey),#f4f4f4);list-style:none;padding:2px 12px 0}
  .offer-list li{font-size:14.5px;font-weight:500;color:var(--ink-grey);line-height:17px;padding:6px 0 7px;border-bottom:1px solid var(--rule-grey)}
  .offer-list li:last-child{border-bottom:none}

  .perks{position:absolute;left:327px;top:380px;width:250px}
  .perk-box{background:var(--navy);color:var(--white);padding:8px 22px;height:56px;margin-bottom:14px}
  .perk-box .small{font-size:13px;font-weight:500;line-height:15px}
  .perk-box .big{font-size:21px;font-weight:700;line-height:24px}
  .perk-box .sub{font-size:14px;font-weight:500;line-height:15px}
  .perk{display:flex;gap:8px;border-bottom:1px solid var(--rule-grey);padding:6px 0 8px;color:var(--ink-grey);font-weight:500;font-size:14.5px;line-height:16px}
  .perk:last-child{border-bottom:none}
  .star{color:var(--leaf-dark);font-weight:700;font-size:22px;line-height:18px;width:18px;flex:none}
  .leads-big{font-family:"Bebas Neue",Impact,sans-serif;font-size:50px;line-height:50px;color:var(--navy);margin-top:4px}
  .ten{display:flex;align-items:center;gap:8px}
  .ten .num{font-family:"Bebas Neue",Impact,sans-serif;font-size:50px;line-height:44px;color:var(--navy)}
  .ten .txt{font-size:18px;line-height:16px;color:var(--ink-grey)}

  .skyline{position:absolute;left:60px;top:742px;width:520px;height:62px;background:linear-gradient(180deg,var(--white),var(--skyline))}

  .license{position:absolute;left:16px;top:804px;width:196px;height:21px;background:var(--footer-ink);color:var(--white);font-size:9.5px;line-height:21px;text-align:center;white-space:nowrap}
  .address{position:absolute;left:218px;top:797px;width:190px;text-align:right;font-style:normal;font-size:12.5px;line-height:15px;color:var(--footer-ink);white-space:nowrap}
  .contact{position:absolute;left:418px;top:797px;width:176px;font-size:12.5px;line-height:15px;color:var(--footer-ink);white-space:nowrap}
</style>
</head>
<body>
  <main class="flyer">
    <section class="hero">
      <div class="brand"><span class="brand-mark"></span><span class="brand-name">Marlow Realty</span></div>
      <div class="hero-art" role="img" aria-label="Illustration of two agents exchanging a house key in front of a modern home with trees"></div>
      <div class="commission">
        <div class="pct">100%</div>
        <div class="line">COMMISSION</div>
        <div class="line">NO MONTHLY FEE</div>
      </div>
      <div class="fee-band">
        <span class="amount">$450</span>
        <span class="label">FLAT<br>TRANSACTION<br>FEE</span>
      </div>
    </section>

    <div class="offer-heading"><h2>WHAT WE OFFER</h2><span class="rule"></span></div>

    <ul class="offer-list">
      <li>24/7 Office Access</li>
      <li>Free E &amp; O Insurance for 1st Year</li>
      <li>Free Online CE and PLE</li>
      <li>Free 1,000 Business Cards</li>
      <li>Free Professional Social Media Marketing</li>
      <li>Free Printing, Scanning, and Copies</li>
      <li>Free Buyer and Seller Presentation Packages</li>
      <li>Free Filquay Cloud Based Document</li>
      <li>Management Access</li>
      <li>Access to our Internal Brokerage Forum</li>
    </ul>

    <aside class="perks">
      <div class="perk-box"><div class="small">COMPANY</div><div class="big">PROFIT SHARING!</div></div>
      <div class="perk-box"><div class="big">PRIVATE OFFICES</div><div class="sub">Available to Rent</div></div>
      <div class="perk"><span class="star">*</span><div>Lead Generation<br>Software with over<div class="leads-big">3,000 LEADS</div></div></div>
      <div class="perk ten"><span class="star">*</span><span class="num">10</span><span class="txt">Leads to<br>Start</span></div>
      <div class="perk"><span class="star">*</span><span>Free Personal CRM and Website</span></div>
      <div class="perk"><span class="star">*</span><span>Restrictions and Rules apply</span></div>
    </aside>

    <div class="skyline" role="img" aria-label="Faint city skyline silhouette"></div>

    <div class="license">Licensed in D.C., Maryland, and Virginia</div>
    <address class="address">4817 Amberfield Road<br>Suite 512, Fairfax, VA 22194</address>
    <div class="contact">T: 703-555-0147<br>E: info@marlowrealty.example</div>
  </main>
</body>
</html>
```